Company Vision Statement Design

I am trying to convert core attributes from our company's vision statement into a graphic:
1. Team
2. Partners (suppliers and customers)
3. Winning
4. Portfolio (diverse offering of beverage products beer, wine, spirits, soft drinks, and water)
5. Profitability
6. Community
I would like to only use pictures as this will accompany the longer descriptions.

Industry/Entity Type

It Company

Font styles to use
Sans Serif

Colors
0355a3

Requirements
Must have
• If there is a base color, I would prefer it is blue to match our company's logo.

```html
<!DOCTYPE html>
<html lang="en">
<head>
<meta charset="utf-8">
<title>Vision Attributes Infographic</title>
<link href="https://fonts.googleapis.com/css2?family=Lato:wght@400;700;900&display=swap" rel="stylesheet">
<style>
  :root{
    --page:#ffffff;
    --panel:#0355a3;
    --disc:#034784;
    --hub:#033f76;
    --ring:#d6e4f2;
    --white:#ffffff;
    --green:#8cc21f;
    --orange:#f7a600;
    --magenta:#e0158f;
    --cyan:#1ab3d9;
    --yellow:#d8d81a;
  }
  html,body{margin:0;padding:0;width:1200px;height:1200px;overflow:hidden;background:var(--page);}
  .canvas{display:block;width:1200px;height:1200px;}
  .panel{fill:var(--panel);}
  .disc{fill:var(--disc);stroke-width:9;}
  .disc.green{stroke:var(--green);}
  .disc.orange{stroke:var(--orange);}
  .disc.magenta{stroke:var(--magenta);}
  .icon{fill:var(--white);}
  .icon-line{fill:none;stroke:var(--white);stroke-width:7;stroke-linecap:round;stroke-linejoin:round;}
  .hub-core{fill:var(--hub);}
  .hub-ring{fill:none;stroke:var(--ring);stroke-width:22;}
  .hand{fill:var(--white);stroke:var(--hub);stroke-width:4;stroke-linejoin:round;}
  .title{font-family:"Lato",sans-serif;font-size:27px;font-weight:700;fill:var(--white);}
</style>
</head>
<body>
<svg class="canvas" viewBox="0 0 1500 1500" xmlns="http://www.w3.org/2000/svg">
  <defs>
    <filter id="lift" x="-30%" y="-30%" width="160%" height="160%">
      <feDropShadow dx="0" dy="6" stdDeviation="8" flood-color="#001a33" flood-opacity=".5"/>
    </filter>
  </defs>

  <rect class="panel" x="182" y="281" width="1135" height="1046"/>

  <!-- colour key -->
  <g class="key">
    <circle cx="1160" cy="370" r="13" fill="var(--yellow)"/>
    <circle cx="1195" cy="370" r="13" fill="var(--orange)"/>
    <circle cx="1230" cy="370" r="13" fill="var(--cyan)"/>
    <circle cx="1265" cy="370" r="13" fill="var(--magenta)"/>
  </g>

  <!-- connectors -->
  <g stroke-width="2">
    <line x1="749" y1="654" x2="749" y2="590" stroke="var(--green)"/>
    <line x1="894.5" y1="738" x2="949.9" y2="706" stroke="var(--magenta)"/>
    <line x1="894.5" y1="906" x2="949.9" y2="938" stroke="var(--orange)"/>
    <line x1="749" y1="990" x2="749" y2="1054" stroke="var(--green)"/>
    <line x1="603.5" y1="906" x2="548.1" y2="938" stroke="var(--magenta)"/>
    <line x1="603.5" y1="738" x2="548.1" y2="706" stroke="var(--orange)"/>
  </g>

  <!-- hub: partnership -->
  <g class="hub" filter="url(#lift)">
    <circle class="hub-core" cx="749" cy="822" r="165"/>
    <circle class="hub-ring" cx="749" cy="822" r="158"/>
  </g>
  <g class="hub-dots">
    <circle cx="749" cy="664" r="5" fill="var(--green)"/>
    <circle cx="885.8" cy="743" r="5" fill="var(--magenta)"/>
    <circle cx="885.8" cy="901" r="5" fill="var(--orange)"/>
    <circle cx="749" cy="980" r="5" fill="var(--green)"/>
    <circle cx="612.2" cy="901" r="5" fill="var(--magenta)"/>
    <circle cx="612.2" cy="743" r="5" fill="var(--orange)"/>
  </g>
  <g class="handshake" transform="translate(749 822)">
    <rect class="hand" x="-118" y="-44" width="28" height="66" rx="4" transform="rotate(-18 -104 -11)"/>
    <rect class="hand" x="90" y="-44" width="28" height="66" rx="4" transform="rotate(18 104 -11)"/>
    <path class="hand" d="M-86 -36 L-30 -52 Q-12 -56 4 -44 L38 -18 Q46 -8 36 0 Q28 4 20 -2 L-8 -22 L-86 20 Z"/>
    <path class="hand" d="M86 -36 L44 -48 Q34 -50 24 -44 L-24 -12 Q-34 -2 -24 8 Q-16 14 -6 8 Q-2 22 12 18 Q18 30 30 24 Q38 32 50 24 L86 20 Z"/>
  </g>

  <!-- Team -->
  <g class="attr team" transform="translate(749 492)">
    <circle class="disc green" r="98" filter="url(#lift)"/>
    <rect class="icon" x="-15" y="-48" width="30" height="22" rx="2"/>
    <path class="icon-line" d="M0 -26 V-12 M-38 -12 H38 M-38 -12 V12 M0 -12 V12 M38 -12 V12" style="stroke-width:5"/>
    <rect class="icon" x="-51" y="12" width="26" height="22" rx="2"/>
    <rect class="icon" x="-13" y="12" width="26" height="22" rx="2"/>
    <rect class="icon" x="25" y="12" width="26" height="22" rx="2"/>
  </g>

  <!-- Partners -->
  <g class="attr partners" transform="translate(1035 657)">
    <circle class="disc magenta" r="98" filter="url(#lift)"/>
    <path class="icon-line" d="M-38 -14 H34 M20 -30 L36 -14 L20 2"/>
    <path class="icon-line" d="M38 18 H-34 M-20 2 L-36 18 L-20 34"/>
  </g>

  <!-- Winning -->
  <g class="attr winning" transform="translate(1035 987)">
    <circle class="disc orange" r="98" filter="url(#lift)"/>
    <polygon class="icon" points="0,-46 11,-15 44,-14 18,6 27,38 0,19 -27,38 -18,6 -44,-14 -11,-15"/>
  </g>

  <!-- Portfolio -->
  <g class="attr portfolio" transform="translate(749 1152)">
    <circle class="disc green" r="98" filter="url(#lift)"/>
    <path class="icon" d="M-4 4 L-4 -34 A38 38 0 1 0 34 4 Z"/>
    <path class="icon" d="M4 -4 L4 -42 A38 38 0 0 1 42 -4 Z"/>
  </g>

  <!-- Profitability -->
  <g class="attr profit" transform="translate(463 987)">
    <circle class="disc magenta" r="98" filter="url(#lift)"/>
    <rect class="icon" x="-40" y="20" width="16" height="20"/>
    <rect class="icon" x="-18" y="6" width="16" height="34"/>
    <rect class="icon" x="4" y="-8" width="16" height="48"/>
    <rect class="icon" x="26" y="-22" width="16" height="62"/>
    <path class="icon-line" d="M-42 -10 L-14 -30 L6 -20 L32 -42" style="stroke-width:5"/>
    <polygon class="icon" points="44,-52 24,-46 38,-32"/>
  </g>

  <!-- Community -->
  <g class="attr community" transform="translate(463 657)">
    <circle class="disc orange" r="98" filter="url(#lift)"/>
    <path class="icon-line" d="M-44 -4 L0 -42 L44 -4" style="stroke-width:8"/>
    <path class="icon" d="M-30 -8 L0 -34 L30 -8 V40 H10 V16 H-10 V40 H-30 Z"/>
  </g>

  <!-- footer title -->
  <text class="title" x="231" y="1271">OUR VISION</text>
</svg>
</body>
</html>
```